Business Card Design Project

We need a business card to reflect the design of our website - just so it all ties in - it has a retro feel and can be found at http://www.velorasoulpair.com
We will need our phone 0437 215 964
Web address, and email velorapair@fernmail.com included
Our catch cry is "Classic Cocktail Music"
Perfect Live Music for Private & Corporate Events, Weddings and Dinner Music
Our names should be included :-
Maribel Thorne / piano & Dennis Holloway / bass
I am now also including our logo so that it can be included (in part or whole) somehow in the design
My partner thinks we should include our logo in some form in the design of the card - i will attach this here for you. I will attach eps but if you prefer another format please let me know
Regards
Mari

```html
<!DOCTYPE html>
<html lang="en">
<head>
<meta charset="utf-8">
<title>Velora Duo – Business Card</title>
<link href="https://fonts.googleapis.com/css2?family=Poiret+One&family=Dosis:wght@500;600;700&family=Oswald:wght@500;600&display=swap" rel="stylesheet">
<style>
  :root {
    --backdrop: #c9c9c9;
    --teal: #7db6b3;
    --teal-deep: #6aa6a3;
    --coral: #d97a57;
    --cream: #ece4c9;
    --cream-panel: #d9d4bf;
    --charcoal: #3a3a3a;
    --orange: #e2603a;
    --rule: #8a877c;
  }
  * { box-sizing: border-box; margin: 0; padding: 0; }
  html, body { width: 1200px; height: 900px; overflow: hidden; }
  body {
    background: var(--backdrop);
    font-family: "Dosis", "Trebuchet MS", sans-serif;
    position: relative;
  }
  .card {
    position: absolute;
    top: 300px;
    width: 520px;
    height: 297px;
    overflow: hidden;
    box-shadow: 0 6px 16px rgba(0,0,0,0.22);
  }

  /* ---------- Front ---------- */
  .card-front { left: 50px; background: var(--teal); }
  .card-front .base-band {
    position: absolute; left: 0; right: 0; bottom: 0; height: 54px;
    background: var(--coral);
  }
  .card-front .flap-stitch { position: absolute; inset: 0; }
  .card-front .emblem {
    position: absolute; left: 236px; top: 46px; width: 48px; height: 48px;
    border-radius: 50%; background: var(--charcoal);
    border: 3px solid var(--cream);
  }
  .card-front .brand-name {
    position: absolute; left: 0; right: 0; top: 100px;
    text-align: center;
    font-family: "Poiret One", "Didot", sans-serif;
    font-size: 62px; letter-spacing: 3px;
    color: var(--cream);
  }
  .card-front .tagline-row {
    position: absolute; left: 40px; right: 40px; top: 190px;
    display: flex; align-items: center; gap: 12px;
  }
  .card-front .dot-rule {
    flex: 1; border-top: 2px dotted var(--cream); opacity: 0.9;
  }
  .card-front .ribbon {
    background: var(--cream);
    color: var(--charcoal);
    font-family: "Oswald", sans-serif; font-weight: 600;
    font-size: 13px; letter-spacing: 1.5px;
    padding: 5px 16px;
    clip-path: polygon(0 0, 100% 0, 94% 50%, 100% 100%, 0 100%, 6% 50%);
    padding-left: 22px; padding-right: 22px;
  }

  /* ---------- Back ---------- */
  .card-back { left: 630px; background: var(--charcoal); }
  .card-back .service-panel {
    position: absolute; left: 0; right: 0; top: 0; height: 108px;
    background: var(--cream-panel);
  }
  .card-back .service-list {
    position: absolute; left: 30px; right: 30px; top: 8px;
    display: flex; justify-content: space-between;
  }
  .service { width: 90px; text-align: center; }
  .service-title {
    font-family: "Oswald", sans-serif; font-weight: 600;
    font-size: 11px; letter-spacing: 0.5px; color: var(--charcoal);
    line-height: 1;
  }
  .service-note {
    font-family: "Oswald", sans-serif; font-weight: 500;
    font-size: 7px; color: var(--charcoal); text-transform: uppercase;
    line-height: 1.1; margin-top: 2px; height: 16px;
  }
  .service-icon {
    width: 40px; height: 40px; margin: 4px auto 0; border-radius: 50%;
    background: var(--orange); border: 2px solid var(--charcoal);
    display: flex; align-items: center; justify-content: center;
  }
  .service-rule { width: 44px; margin: 8px auto 0; border-top: 2px solid var(--rule); }

  .card-back .details {
    position: absolute; left: 0; right: 0; top: 114px;
    text-align: center;
  }
  .headline { color: var(--orange); font-weight: 600; font-size: 17px; line-height: 1.1; }
  .occasions { color: var(--cream); font-weight: 500; font-size: 12.5px; margin-top: 1px; }
  .players {
    display: inline-block; margin-top: 5px; padding: 2px 10px;
    border: 1px solid #777; border-radius: 4px;
    font-weight: 700; font-size: 15px; letter-spacing: 0.4px;
    color: var(--cream); text-transform: uppercase;
  }
  .players .player-name, .players .instrument-last { color: var(--teal); }
  .phone { color: var(--cream); font-weight: 600; font-size: 22px; letter-spacing: 1px; margin-top: 2px; }
  .contact-line { color: var(--cream); font-weight: 500; font-size: 14px; margin-top: 1px; }
  .contact-line .site-name { color: var(--orange); }
  .card-back .base-band {
    position: absolute; left: 0; right: 0; bottom: 0; height: 34px;
    background: var(--teal);
  }
</style>
</head>
<body>

  <section class="card card-front" aria-label="Card front">
    <div class="base-band"></div>
    <svg class="flap-stitch" width="520" height="297" viewBox="0 0 520 297" aria-hidden="true">
      <path d="M0 52 H220 Q228 52 228 62 Q230 106 260 106 Q290 106 292 62 Q292 52 300 52 H520"
            fill="none" stroke="#5f9895" stroke-width="1.2"/>
      <path d="M0 56 H216 Q224 56 224 66 Q228 110 260 110 Q292 110 296 66 Q296 56 304 56 H520"
            fill="none" stroke="#a3d0cd" stroke-width="1" stroke-dasharray="3 3"/>
      <line x1="0" y1="243" x2="520" y2="243" stroke="#e8a98e" stroke-width="1" stroke-dasharray="3 3"/>
    </svg>
    <div class="emblem"></div>
    <h1 class="brand-name">VELORA DUO</h1>
    <div class="tagline-row">
      <span class="dot-rule"></span>
      <span class="ribbon">CLASSIC COCKTAIL MUSIC</span>
      <span class="dot-rule"></span>
    </div>
  </section>

  <section class="card card-back" aria-label="Card back">
    <div class="service-panel"></div>
    <ul class="service-list" style="list-style:none">
      <li class="service">
        <div class="service-title">WEDDINGS</div>
        <div class="service-note">Ceremony &amp;<br>reception</div>
        <div class="service-icon">
          <svg width="22" height="22" viewBox="0 0 22 22" aria-hidden="true">
            <rect x="3" y="2" width="16" height="18" fill="none" stroke="#3a3a3a" stroke-width="2"/>
            <rect x="7" y="5" width="8" height="12" fill="#3a3a3a"/>
          </svg>
        </div>
        <div class="service-rule"></div>
      </li>
      <li class="service">
        <div class="service-title">PACKAGES</div>
        <div class="service-note">Cover the whole<br>event</div>
        <div class="service-icon">
          <svg width="22" height="22" viewBox="0 0 22 22" aria-hidden="true">
            <circle cx="11" cy="8" r="6" fill="#3a3a3a"/>
            <rect x="8" y="13" width="6" height="6" fill="#3a3a3a"/>
          </svg>
        </div>
        <div class="service-rule"></div>
      </li>
      <li class="service">
        <div class="service-title">CORPORATE</div>
        <div class="service-note">All events in<br>QLD</div>
        <div class="service-icon">
          <svg width="22" height="22" viewBox="0 0 22 22" aria-hidden="true">
            <path d="M2 11 L8 6 L14 9 L20 6 M2 11 L9 17 L20 10" fill="none" stroke="#3a3a3a" stroke-width="3" stroke-linejoin="round"/>
          </svg>
        </div>
        <div class="service-rule"></div>
      </li>
      <li class="service">
        <div class="service-title">PRIVATE</div>
        <div class="service-note">Parties &amp;<br>speciality</div>
        <div class="service-icon">
          <svg width="24" height="24" viewBox="0 0 24 24" aria-hidden="true">
            <g fill="none" stroke="#3a3a3a" stroke-width="1.6">
              <ellipse cx="12" cy="12" rx="10" ry="4"/>
              <ellipse cx="12" cy="12" rx="10" ry="4" transform="rotate(60 12 12)"/>
              <ellipse cx="12" cy="12" rx="10" ry="4" transform="rotate(-60 12 12)"/>
            </g>
            <circle cx="12" cy="12" r="2" fill="#3a3a3a"/>
          </svg>
        </div>
        <div class="service-rule"></div>
      </li>
    </ul>

    <div class="details">
      <p class="headline">Perfect Live Music for</p>
      <p class="occasions">Private &amp; Corporate Events, Weddings and Dinner Music</p>
      <p class="players">
        <span class="player-name">Maribel Thorne</span> / Piano &amp;
        <span class="player-name">Dennis Holloway</span> / <span class="instrument-last">Bass</span>
      </p>
      <p class="phone">0437 215 964</p>
      <p class="contact-line">velorapair@fernmail.com / www.<span class="site-name">velorasoulpair</span>.com</p>
    </div>
    <div class="base-band"></div>
  </section>

</body>
</html>
```